Business card design needed

I need a business card design for a dog walking, dog minding and dog training business. Please refer to my website for the basic company colours and fonts I'm after. Planning on a double sided card, so all information doesn't need to be on the 'front' side.
Cheers

Industry/Entity Type

Dog Training

Contact Information for Business Card

Meadow Paws - happy hounds
Rua 0498307164
meadowpawsdemo.com.au
-walking
-holiday stays
-onsite care
-training and behavioural consultations

```html
<!DOCTYPE html>
<html lang="en">
<head>
<meta charset="utf-8">
<title>Meadow Paws – Business Card</title>
<link href="https://fonts.googleapis.com/css2?family=Federo&display=swap" rel="stylesheet">
<style>
  :root {
    --bg-top: #8c7f7e;
    --bg-bottom: #d5603a;
    --orange: #e05a27;
    --orange-soft: #ea7d4f;
    --grey-text: #707070;
    --charcoal: #2b2b2b;
    --slate: #565656;
    --white: #ffffff;
  }
  html, body {
    margin: 0;
    width: 1200px;
    height: 1000px;
    overflow: hidden;
  }
  body {
    position: relative;
    background: linear-gradient(180deg, var(--bg-top) 0%, var(--bg-bottom) 100%);
    font-family: "Federo", sans-serif;
  }
  .card {
    position: absolute;
    left: 222px;
    width: 734px;
    border-radius: 6px;
    overflow: hidden;
    background: var(--white);
  }
  .card--front { top: 50px; height: 398px; }
  .card--back { top: 475px; height: 399px; }

  /* front */
  .front-header {
    position: absolute; left: 0; top: 0; width: 100%; height: 113px;
    background: linear-gradient(180deg, #ffffff 0%, #ececec 100%);
  }
  .brand-name {
    position: absolute; left: 24px; top: 40px;
    font-size: 32px; color: var(--orange); letter-spacing: 1px; line-height: 1;
    white-space: nowrap;
  }
  .header-silhouettes {
    position: absolute; left: 295px; top: 70px; width: 300px; height: 36px;
    background: linear-gradient(90deg, rgba(200,200,200,0) 0%, rgba(190,190,190,.45) 50%, rgba(200,200,200,0) 100%);
  }
  .header-puppy {
    position: absolute; left: 592px; top: 30px; width: 130px; height: 80px;
    border-radius: 40px 40px 6px 6px;
    background: radial-gradient(circle at 50% 45%, #b76a3a 0%, #e8d9cc 60%, #f6f2ee 100%);
  }
  .header-band-edge {
    position: absolute; top: 100px; width: 6px; height: 50px; background: var(--charcoal);
  }
  .header-band-edge--left { left: 0; }
  .header-band-edge--right { right: 0; }
  .header-band {
    position: absolute; left: 6px; top: 113px; width: 722px; height: 37px; background: var(--orange);
  }
  .contact-box {
    position: absolute; left: 25px; top: 185px; width: 289px; height: 157px;
    border-radius: 4px; overflow: hidden; background: var(--orange);
  }
  .contact-box::before {
    content: ""; position: absolute; left: -60px; top: -230px; width: 410px; height: 320px;
    border-radius: 50%; background: var(--orange-soft);
  }
  .name-pill {
    position: absolute; left: 9px; top: 9px; width: 148px; height: 36px;
    background: var(--white); border-radius: 5px;
    font-size: 21px; color: var(--orange-soft); line-height: 36px; text-align: center;
  }
  .name-pill span { color: var(--grey-text); }
  .phone {
    position: absolute; left: 28px; top: 57px; font-size: 18px; color: var(--white);
  }
  .web-label {
    position: absolute; left: 0; width: 100%; top: 103px; text-align: center;
    font-size: 15px; color: var(--charcoal);
  }
  .web-label span { color: var(--white); }
  .web-pill {
    position: absolute; left: 34px; top: 126px; width: 188px; height: 24px;
    background: var(--white); border-radius: 5px;
    font-size: 12px; color: var(--orange); line-height: 24px; text-align: center;
    white-space: nowrap;
  }
  .photo-collage {
    position: absolute; left: 382px; top: 163px; width: 301px; height: 234px;
    background: linear-gradient(135deg, #8d9a7a 0%, #6d5a46 45%, #7e8e92 75%, #5d6b3e 100%);
    opacity: .85;
  }

  /* back */
  .back-strip {
    position: absolute; left: 0; top: 0; width: 33px; height: 100%;
    background: linear-gradient(180deg, var(--slate) 0 59%, var(--charcoal) 59% 100%);
  }
  .back-brand {
    position: absolute; left: 86px; top: 186px; display: flex; align-items: center; gap: 10px;
    font-size: 30px; color: var(--orange-soft); letter-spacing: 1px; white-space: nowrap;
    line-height: 1;
  }
  .back-brand .mark {
    width: 18px; height: 18px; border-radius: 50%; background: var(--orange-soft);
  }
  .service-panel { position: absolute; left: 0; top: 0; }
  .service {
    position: absolute; color: var(--orange-soft); white-space: nowrap; line-height: 1;
  }
  .service--lg { font-size: 32px; }
  .service--sm { font-size: 18px; }
  .dog-silhouette {
    position: absolute; background: var(--orange-soft); border-radius: 8px;
  }
</style>
</head>
<body>

<section class="card card--front">
  <div class="front-header"></div>
  <div class="header-silhouettes" role="img" aria-label="Faint silhouettes of dogs running"></div>
  <div class="brand-name">MEADOW PAWS</div>
  <div class="header-puppy" role="img" aria-label="Photo of a puppy peeking over the band"></div>
  <div class="header-band-edge header-band-edge--left"></div>
  <div class="header-band-edge header-band-edge--right"></div>
  <div class="header-band"></div>

  <div class="contact-box">
    <div class="name-pill">CANINES <span>RUA</span></div>
    <div class="phone">TEL:0498307164</div>
    <div class="web-label">WEB<span>SITE</span></div>
    <div class="web-pill">MEADOWPAWSDEMO.COM.AU</div>
  </div>

  <div class="photo-collage" role="img" aria-label="Collage of photos of dogs playing outdoors"></div>
</section>

<section class="card card--back">
  <div class="back-strip"></div>

  <div class="back-brand"><span class="mark"></span>MEADOW PAWS</div>

  <svg class="service-panel" width="734" height="399" viewBox="0 0 734 399">
    <path d="M438 0 Q350 200 438 399 L734 399 L734 0 Z" fill="#2b2b2b"/>
    <path d="M438 0 Q368 118 383 237 L734 237 L734 0 Z" fill="#565656"/>
  </svg>

  <div class="service service--lg" style="left:456px; top:20px;">HOLIDAY STAYS</div>
  <div class="dog-silhouette" role="img" aria-label="Silhouette of a leaping dog" style="left:614px; top:64px; width:80px; height:50px;"></div>
  <div class="service service--lg" style="left:460px; top:118px;">ONSITE CARE</div>
  <div class="dog-silhouette" role="img" aria-label="Silhouette of a standing hound" style="left:630px; top:152px; width:84px; height:58px;"></div>
  <div class="service service--lg" style="left:460px; top:195px;">WALKING</div>
  <div class="dog-silhouette" role="img" aria-label="Silhouette of a bulldog" style="left:490px; top:240px; width:84px; height:50px;"></div>
  <div class="service service--sm" style="left:461px; top:296px;">TRAINING AN&nbsp; BEHAVIOURAL</div>
  <div class="service service--sm" style="left:466px; top:324px;">CONSULTATIONS</div>
  <div class="dog-silhouette" role="img" aria-label="Silhouette of a small dog sitting up" style="left:664px; top:332px; width:38px; height:60px;"></div>
</section>

</body>
</html>
```